Bref créative
Brochure for Professional Services Firm
Brightfen Partners
We need a great design for a brochure to be used as marketing collateral at tradeshows and for general marketing purposes. Our website is brightfenpartners.example to get additional information. We generally work with oilfield service companies.
Consulting
Corporate, professional.
===========Update==========
Requirement : Trifold
Our logo files.
Here is a sample presentation we currently use to market our services.
Some stock photos we have.
stock photos.
stock photo.

```html
<!DOCTYPE html>
<html lang="en">
<head>
<meta charset="utf-8">
<title>Brightfen Partners – Trifold Brochure</title>
<link rel="stylesheet" href="https://fonts.googleapis.com/css2?family=Open+Sans:wght@400;600;700&family=Montserrat:wght@600;700&display=swap">
<style>
  :root{
    --bg:#e6e7e9;
    --blue:#2fa8e0;
    --blue-deep:#1b7fb4;
    --charcoal:#2a2c30;
    --charcoal-2:#3a3d42;
    --photo-sky:#c9d8e4;
    --photo-steel:#5f6f7d;
    --white:#ffffff;
    --text-dark:#33363b;
    --text-soft:#c9ced4;
  }
  *{box-sizing:border-box;margin:0;padding:0}
  html,body{width:1200px;height:842px;overflow:hidden}
  body{background:var(--bg);font-family:"Open Sans",Arial,sans-serif;position:relative}
  .spread{position:absolute;top:198px;width:576px;height:446px;display:flex;box-shadow:0 6px 18px rgba(0,0,0,.18);background:var(--white)}
  .spread--outside{left:16px}
  .spread--inside{left:608px}
  .panel{position:relative;width:192px;height:100%;overflow:hidden}
  .panel + .panel{border-left:1px solid rgba(0,0,0,.06)}
  .photo{position:absolute;left:0;right:0}
  .brand{display:flex;align-items:center;gap:7px;font-family:"Montserrat",Arial,sans-serif;font-weight:700;color:var(--charcoal);font-size:15px;letter-spacing:.06em;text-transform:uppercase}
  .brand__mark{width:11px;height:11px;background:var(--blue)}
  .dark-band{position:absolute;left:0;right:0;bottom:0;background:var(--charcoal)}
  .small-text{font-size:8px;line-height:1.45;color:var(--text-soft)}
  .heading{font-family:"Montserrat",Arial,sans-serif;font-weight:700;text-transform:uppercase;letter-spacing:.04em}

  /* outside: about panel */
  .about__photo{top:0;height:150px;background:linear-gradient(180deg,var(--photo-sky),var(--photo-steel))}
  .about__title{position:absolute;top:128px;left:14px;color:var(--white);font-size:17px}
  .about__body{position:absolute;top:156px;left:0;right:0;bottom:0;background:var(--blue);padding:16px 14px;color:var(--white);font-size:8.5px;line-height:1.55}

  /* outside: back panel */
  .back__photo{top:0;height:170px;background:linear-gradient(180deg,#dfe5ea,#7d8a95)}
  .back__band{position:absolute;top:170px;left:0;right:0;height:40px;background:var(--blue)}
  .back__dark{top:210px;padding:18px 16px}
  .service-list{list-style:none}
  .service-list li{display:flex;align-items:center;gap:7px;font-size:8.5px;color:var(--text-soft);margin-bottom:9px}
  .service-list li::before{content:"";width:5px;height:5px;background:var(--blue)}
  .back__site{position:absolute;bottom:18px;left:16px;font-size:8.5px;color:var(--blue);font-weight:600}

  /* outside: cover */
  .cover__brand{position:absolute;top:26px;left:22px}
  .cover__photo{top:70px;height:220px;background:linear-gradient(180deg,#eef2f5,#8a98a4 70%,#4d5964)}
  .cover__frames{position:absolute;top:60px;left:0}
  .cover__dark{top:290px;padding:22px 18px}
  .cover__tag{font-size:9px;color:var(--text-soft);letter-spacing:.03em}
  .cover__rule{width:40px;height:3px;background:var(--blue);margin-top:10px}

  /* inside */
  .inside__photo-left{top:0;bottom:0;background:linear-gradient(180deg,#bcd6ea 0%,#dfe8ef 45%,#7a6e62 100%)}
  .inside__photo-wide{position:absolute;top:0;left:192px;width:384px;height:170px;background:linear-gradient(90deg,#aec3d3,#e9eef2 60%,#c7d3dc)}
  .inside__text{position:absolute;top:184px;left:0;right:0;padding:0 14px;color:var(--text-dark)}
  .inside__text .heading{font-size:11px;color:var(--blue-deep);margin-bottom:8px}
  .inside__text p{font-size:8.5px;line-height:1.55}
  .inside__accent{position:absolute;bottom:0;left:0;right:0;height:8px;background:var(--blue)}
</style>
</head>
<body>

<section class="spread spread--outside" aria-label="Brochure outside spread">
  <article class="panel panel--about">
    <div class="photo about__photo" role="img" aria-label="Oilfield pumpjack photo"></div>
    <h2 class="heading about__title">About Us</h2>
    <div class="about__body">
      We help oilfield service companies grow with clear strategy, sound finance and steady operations. Our partners bring years of field and boardroom experience to every engagement.
    </div>
  </article>

  <article class="panel panel--back">
    <div class="photo back__photo" role="img" aria-label="Drilling equipment photo"></div>
    <div class="back__band"></div>
    <div class="dark-band back__dark" style="height:236px">
      <ul class="service-list">
        <li>Strategy &amp; Planning</li>
        <li>Financial Advisory</li>
        <li>Operations Review</li>
      </ul>
      <div class="back__site">brightfenpartners.example</div>
    </div>
  </article>

  <article class="panel panel--cover">
    <div class="brand cover__brand"><span class="brand__mark"></span>Brightfen</div>
    <div class="photo cover__photo" role="img" aria-label="Pumpjack against the sky photo"></div>
    <svg class="cover__frames" width="192" height="240" viewBox="0 0 192 240" aria-hidden="true">
      <g fill="none" stroke="var(--blue)" stroke-width="3">
        <polyline points="10,30 70,30 70,110 130,110 130,60 182,60"/>
        <polyline points="40,230 40,150 110,150 110,200 170,200 170,120"/>
      </g>
      <rect x="0" y="200" width="60" height="30" fill="var(--blue)" opacity=".85"/>
    </svg>
    <div class="dark-band cover__dark" style="height:156px">
      <p class="cover__tag">Consulting for oilfield service companies</p>
      <div class="cover__rule"></div>
    </div>
  </article>
</section>

<section class="spread spread--inside" aria-label="Brochure inside spread">
  <article class="panel">
    <div class="photo inside__photo-left" role="img" aria-label="Drilling rig with crew photo"></div>
  </article>
  <div class="inside__photo-wide" role="img" aria-label="Silhouettes of two workers near a pumpjack photo"></div>
  <article class="panel">
    <div class="inside__text">
      <h3 class="heading">Our Approach</h3>
      <p>We start by listening. Every engagement begins with a close look at your crews, your equipment and your markets, so our advice fits the way you work.</p>
    </div>
    <div class="inside__accent"></div>
  </article>
  <article class="panel">
    <div class="inside__text">
      <h3 class="heading">What We Do</h3>
      <p>From budgeting to field performance, we give leaders the numbers and the plan they need to move forward with confidence.</p>
      <h3 class="heading" style="margin-top:14px">Why Brightfen</h3>
      <p>Lean teams, direct access to partners and results you can measure.</p>
    </div>
    <div class="inside__accent"></div>
  </article>
</section>

</body>
</html>
```